Media/PR business needs a website upgrade

Modernise my website www.pvl.net.au into a simpler and mobile friendly site with the usual plugins, maximum 5 pages, 4 might be enough. My page is already hosted and I have an email address so I just want to work with a designer who is fantastic with WordPress, to refresh and simplify the 6 year-old look.

Target Market(s)

men & women 25-55

Industry/Entity Type

Business

Coding

Coded - Design and coding required

Number of Pages Required

4 page

Font styles to use
Sans Serif

Colors
f37122
ffffff

Requirements
Must have
• Social media plugins, about, client portfolio, contact (can be under about)blog capability
Nice to have
• photos of jobs I've done
Should not have
• e-commerce, can lose all the client logos

```html
<!DOCTYPE html>
<html lang="en">
<head>
<meta charset="utf-8">
<title>Pivot Lane Communications – Public Relations &amp; Event Management</title>
<link href="https://fonts.googleapis.com/css2?family=Kreon:wght@300;400;600&family=Open+Sans:wght@300;400;600&display=swap" rel="stylesheet">
<style>
  :root {
    --brand-orange: #f37122;
    --button-orange: #f7941d;
    --ink: #333333;
    --ink-soft: #444444;
    --muted-icon: #8a8a8a;
    --white: #ffffff;
    --hero-sand: #d9d1c4;
    --hero-sand-dark: #c9bfae;
  }
  * { box-sizing: border-box; margin: 0; padding: 0; }
  html, body {
    width: 1200px;
    height: 1182px;
    overflow: hidden;
    background: var(--white);
    font-family: "Open Sans", Arial, sans-serif;
    color: var(--ink);
  }
  .page { position: relative; width: 1200px; height: 1182px; overflow: hidden; }

  /* Header */
  .site-header { position: absolute; top: 0; left: 0; width: 1200px; height: 96px; background: var(--white); }
  .brand { position: absolute; left: 130px; top: 18px; display: flex; align-items: center; gap: 8px; }
  .brand-dot { width: 62px; height: 62px; border-radius: 50%; background: var(--brand-orange); }
  .brand-name {
    font-family: "Kreon", Georgia, serif; font-weight: 600; font-size: 16px;
    line-height: 15px; color: var(--ink);
  }
  .social-links { position: absolute; top: 22px; left: 822px; display: flex; gap: 12px; }
  .social-links span { width: 13px; height: 13px; border-radius: 50%; background: var(--muted-icon); display: block; }
  .phone {
    position: absolute; top: 18px; left: 940px; display: flex; align-items: center; gap: 4px;
    font-size: 19px; color: var(--ink);
  }
  .main-nav { position: absolute; top: 64px; left: 517px; display: flex; gap: 32px; font-size: 13px; }
  .main-nav a { color: var(--ink); text-decoration: none; position: relative; padding-bottom: 19px; }
  .main-nav a.active::after {
    content: ""; position: absolute; left: -5px; right: 0; bottom: 0; height: 3px; background: var(--button-orange);
  }

  /* Hero */
  .hero {
    position: absolute; top: 96px; left: 0; width: 1200px; height: 620px;
    background: linear-gradient(90deg, var(--hero-sand) 0%, var(--hero-sand-dark) 100%);
  }
  .hero-portrait {
    position: absolute; right: 0; top: 0; width: 620px; height: 620px;
    background: linear-gradient(180deg, #cfc4b3 0%, #b9ad9c 40%, #3a7bc8 75%, #2f6db8 100%);
  }
  .hero-copy { position: absolute; left: 140px; top: 182px; }
  .hero-title {
    font-family: "Kreon", Georgia, serif; font-weight: 600; font-size: 40px;
    line-height: 47px; color: var(--ink);
  }
  .hero-sub {
    margin-top: 12px; margin-left: 3px; font-family: "Kreon", Georgia, serif; font-weight: 400;
    font-size: 22px; line-height: 26px; color: var(--ink-soft);
  }
  .btn-learn {
    display: inline-block; margin-top: 20px; margin-left: 2px; width: 127px; height: 40px; line-height: 40px;
    text-align: center; background: var(--button-orange); color: var(--white);
    font-size: 11px; text-transform: uppercase; text-decoration: none;
  }

  /* Intro */
  .intro { position: absolute; top: 806px; left: 140px; width: 490px; }
  .intro-lead {
    font-family: "Kreon", Georgia, serif; font-weight: 300; font-size: 27px; line-height: 35px;
    color: var(--button-orange);
  }
  .intro-body { margin-top: 29px; margin-left: 3px; font-size: 12.5px; font-weight: 300; line-height: 19.5px; color: var(--ink); }
  .intro-body p + p { margin-top: 19px; }
  .features { position: absolute; top: 1155px; left: 145px; display: flex; }
  .feature { width: 167px; font-size: 11px; line-height: 13px; text-transform: uppercase; color: var(--ink); }

  /* Job photos */
  .job-photo { position: absolute; width: 192px; box-shadow: 0 6px 16px rgba(0,0,0,0.12); }
  .photo-phone { left: 865px; top: 818px; height: 192px; background: linear-gradient(135deg, #c9b8a6, #efe9e2); }
  .photo-mics { left: 656px; top: 914px; height: 192px; background: linear-gradient(135deg, #3d55c2, #f0ede9 60%, #8a8f99); }
  .photo-meeting { left: 865px; top: 1026px; height: 160px; background: linear-gradient(135deg, #7ea38e, #e7e2da 60%, #4a4a4a); }
  .photo-stripes { left: 656px; top: 1122px; height: 64px; background: linear-gradient(90deg, #1f2b4a, #e9e6ea 60%, #b06a4a); }
</style>
</head>
<body>
<div class="page">
  <header class="site-header">
    <div class="brand">
      <div class="brand-dot"></div>
      <div class="brand-name">Pivot<br>Lane<br>Communications</div>
    </div>
    <div class="social-links" aria-label="Social media links"><span></span><span></span><span></span><span></span></div>
    <div class="phone">
      <svg width="14" height="18" viewBox="0 0 14 18" aria-hidden="true"><path d="M3 1 L6 1 L7 5 L5 6.5 Q6 10.5 9 12.5 L10.5 10.8 L13.5 12.5 L13 16 Q11 17.5 8 16 Q1.5 12 1 4 Z" fill="#333"/></svg>
      0400 615 237
    </div>
    <nav class="main-nav">
      <a class="active" href="#">Home</a>
      <a href="#">Services</a>
      <a href="#">About</a>
      <a href="#">Client Portfolio</a>
      <a href="#">Testimonials</a>
      <a href="#">Blog</a>
      <a href="#">Contact</a>
    </nav>
  </header>

  <section class="hero">
    <div class="hero-portrait" role="img" aria-label="Portrait of the founder smiling, wearing a blue t-shirt and light grey jacket"></div>
    <div class="hero-copy">
      <h1 class="hero-title">Public Relations &amp;<br>Event Management Business</h1>
      <p class="hero-sub">Flexible, composed and relationship focused<br>freelancer ready to start work.</p>
      <a class="btn-learn" href="#">Learn More</a>
    </div>
  </section>

  <section class="intro">
    <h2 class="intro-lead">Pivot Lane Communications is an established specialist public relations and event management business.</h2>
    <div class="intro-body">
      <p>With a communications degree and 20 plus years experience working in public relations, publicity, media and project management, PLC founder Dana Whitford offers a complete contract based option for your next major sporting, social, cultural or community event.</p>
      <p>Contact Dana at PLC for strategic advice on sponsorship spend and how to leverage your investment, and to tap into her extensive media and professional network.</p>
      <p>Flexible, composed and relationship focused freelancer ready to start work.</p>
    </div>
  </section>

  <div class="features">
    <div class="feature" style="width:208px">Contrary to<br>popular belief</div>
    <div class="feature" style="width:170px">Lorem ipsum<br>is simply dummy</div>
    <div class="feature">Map lorem<br>ipsum is simply</div>
  </div>

  <div class="job-photo photo-phone" role="img" aria-label="Woman taking notes during a phone call at an office desk"></div>
  <div class="job-photo photo-mics" role="img" aria-label="Press conference microphones lined up on a podium"></div>
  <div class="job-photo photo-meeting" role="img" aria-label="Small team meeting around a table with laptops"></div>
  <div class="job-photo photo-stripes" role="img" aria-label="Person in a striped top at an event"></div>
</div>
</body>
</html>
```